Veltiwell- Comprehensive quality healthcare delivered at your door.

I am looking for brochures to help promote my business. My business name is Veltiwel (see attachment and logo). This is a new health delivery system designed to provide high quality care to elderly in their communities or at home.

See attachements. The logo is already designed.

As far as services provided (see attachment)

Target Market(s)

Elderly patients

Industry/Entity Type

Business

Font styles to use
Serif

Colors

Designer to choose colors to be used in the design.

```html
<!DOCTYPE html>
<html lang="en">
<head>
<meta charset="utf-8">
<title>Veltiwel – Home and Community Based Services</title>
<link rel="stylesheet" href="https://fonts.googleapis.com/css2?family=Lora:wght@400;600&display=swap">
<style>
  :root {
    --green-deep: #2f4a12;
    --green-mid: #4f7a17;
    --green-bright: #7cb518;
    --orange: #f08a12;
    --orange-red: #e2511f;
    --ink: #1c1c1c;
    --paper: #ffffff;
  }
  html, body { margin: 0; padding: 0; overflow: hidden; background: var(--paper); }
  .brochure {
    position: relative;
    width: 855px;
    height: 1200px;
    overflow: hidden;
    background: var(--paper);
    font-family: "Lora", Georgia, serif;
    color: var(--ink);
  }
  .top-band, .bottom-band { position: absolute; left: 0; width: 855px; display: block; }
  .top-band { top: 0; height: 140px; }
  .bottom-band { top: 1040px; height: 160px; }

  .brand {
    position: absolute;
    left: 0; top: 104px;
    width: 855px;
    text-align: center;
  }
  .brand-mark {
    width: 160px; height: 160px;
    margin: 0 auto;
    border-radius: 50%;
    background: var(--green-mid);
  }
  .brand-name {
    margin: 6px 0 0;
    font-size: 30px;
    line-height: 36px;
    font-weight: 400;
    letter-spacing: 1px;
    color: var(--green-deep);
  }

  .site-nav {
    position: absolute;
    left: 50px; top: 323px;
    margin: 0; padding: 0;
    list-style: none;
  }
  .site-nav li {
    position: relative;
    padding-left: 52px;
    font-size: 16px;
    line-height: 23.3px;
    color: var(--orange-red);
  }
  .site-nav li::before {
    content: "";
    position: absolute;
    left: 3px; top: 11px;
    width: 3px; height: 3px;
    border-radius: 50%;
    background: var(--orange-red);
  }
  .site-nav sup { font-size: 9px; line-height: 0; }

  .section-title {
    position: absolute;
    left: 51px;
    margin: 0;
    font-size: 15px;
    font-weight: 400;
    color: var(--orange-red);
  }
  .stay-home-title { top: 548px; }
  .services-title { top: 773px; }
  .sites-title { top: 1055px; font-size: 16px; }

  .intro {
    position: absolute;
    left: 51px; top: 576px;
    width: 600px;
    margin: 0;
    font-size: 13.5px;
    line-height: 20px;
  }

  .photo-strip {
    position: absolute;
    left: 102px; top: 624px;
    width: 624px; height: 137px;
    border: 4px solid var(--orange);
    display: flex;
  }
  .photo { flex: 1; height: 100%; }
  .photo-walk { background: linear-gradient(135deg, #6f7f86, #c9ccc4 60%, #8d9a8e); }
  .photo-visit { background: linear-gradient(135deg, #d8d2cc, #f1ece6 55%, #b97a6e); border-left: 2px solid #fff; border-right: 2px solid #fff; }
  .photo-park { background: linear-gradient(135deg, #9a5a2a, #c98a3d 50%, #3b4a55); }

  .service-list {
    position: absolute;
    left: 51px; top: 799px;
    margin: 0; padding: 0;
    list-style: none;
    font-size: 13.5px;
    line-height: 20.1px;
  }

  .site-name {
    position: absolute;
    left: 53px; top: 1078px;
    margin: 0;
    font-size: 13.5px;
    line-height: 18px;
    z-index: 1;
  }

  .footer-brand {
    position: absolute;
    right: 30px; bottom: 38px;
    display: flex;
    align-items: center;
    gap: 8px;
  }
  .footer-mark {
    width: 40px; height: 40px;
    border-radius: 50%;
    background: var(--green-deep);
  }
  .footer-name {
    font-size: 18px;
    color: var(--paper);
  }
</style>
</head>
<body>
<main class="brochure">
  <svg class="top-band" viewBox="0 0 855 140" preserveAspectRatio="none" aria-hidden="true">
    <defs>
      <linearGradient id="topGreen" x1="0" y1="0" x2="1" y2="0">
        <stop offset="0" stop-color="#2f4a12"/>
        <stop offset="0.55" stop-color="#4f7a17"/>
        <stop offset="1" stop-color="#7cb518"/>
      </linearGradient>
    </defs>
    <path d="M0 0 H855 V118 C640 72 360 48 0 80 Z" fill="#f08a12"/>
    <path d="M0 0 H855 V108 C640 62 360 40 0 68 Z" fill="url(#topGreen)"/>
  </svg>

  <header class="brand">
    <div class="brand-mark"></div>
    <p class="brand-name">VELTIWEL</p>
  </header>

  <ul class="site-nav">
    <li>Home</li>
    <li>Assisted Living</li>
    <li>Skilled Nursing</li>
    <li>Independent Living</li>
    <li>Home and Community Based Services</li>
    <li>Respite Care</li>
    <li>Rehabilitation</li>
    <li>NOVRA LearningCenter</li>
    <li>NOVRA Learning<sup>®</sup></li>
  </ul>

  <h2 class="section-title stay-home-title">STAY HOME</h2>
  <p class="intro">Veltiwel offers home and Community Based Services for adults who wish to continue to live independently in the comfort of their communities.</p>

  <div class="photo-strip">
    <div class="photo photo-walk" role="img" aria-label="Caregiver helping an elderly man walk with a frame"></div>
    <div class="photo photo-visit" role="img" aria-label="Nurse sharing a meal and conversation with an elderly woman"></div>
    <div class="photo photo-park" role="img" aria-label="Elderly couple enjoying an autumn park outdoors"></div>
  </div>

  <h2 class="section-title services-title">SERVICES</h2>
  <ul class="service-list">
    <li>Comprehensive primary care services</li>
    <li>Coordination of speciality care</li>
    <li>Chronic disease management such as COPD, Asthma, Diabetes mellitus,</li>
    <li>Heart disease like congestive heart failure, Alzheimer’s dementia, etc…</li>
    <li>Transitional Care</li>
    <li>Skilled nursing visits for wound care, catheter care, ostomy</li>
    <li>Social services assessment</li>
    <li>Home health assistance</li>
    <li>Physical therapy</li>
    <li>Mental health</li>
    <li>Dental health</li>
    <li>Transportation</li>
  </ul>

  <svg class="bottom-band" viewBox="0 0 855 160" preserveAspectRatio="none" aria-hidden="true">
    <path d="M0 72 C280 42 580 16 855 6 V160 H0 Z" fill="#2f4a12"/>
    <path d="M0 84 C280 54 580 30 855 22 V160 H0 Z" fill="#f08a12"/>
  </svg>

  <h2 class="section-title sites-title">Sites of Operations</h2>
  <p class="site-name">Still Meadow</p>

  <footer class="footer-brand">
    <div class="footer-mark"></div>
    <span class="footer-name">Veltiwel</span>
  </footer>
</main>
</body>
</html>
```